依頼詳細
トップページのデザイン トップページとサブページ(2ページ目以降)のデザイン サブページは、トップページのデザインを引き継ぐ感じで
グローバルナビ  ワードプレス×レスポンシブで制作予定

全体的なイメージ https://www.morino-kobo.jp/index.html
青とホワイトを基調にした清潔感があり ごちゃごちゃしすぎず
患者さんの視線で見やすく 探しやすい感じを希望します。
お子様や女性にも好まれるような可愛いイラストなどもお願いします。

グローバルナビに入れる予定の項目 Q&A、アクセス、医院紹介、治療内容、マウスピース矯正、費用、部分矯正、裏側矯正

トップページに記載したい文章
マウスピース型矯正装置(クリアフィット)をメインの紹介するサイト
裏側矯正にも力入れており、見えないMIX (マウスピース矯正と裏側矯正の組み合わせで幅広く対応できる。

最新式 デジタルスキャナー dento scope の紹介
参考https://hanawa-dent.jp/orthodontic/clearfit/

ブログ形式で 新着情報
休診日・診療時間/
ご相談・お問い合わせ

希望イメージ
シンプル 複雑
単色 カラフル
暗い 明るい
日常 高級
遊び心 厳粛
未来的 伝統的
女性的 男性的
希望する色
水色系
納品ファイル
• 高解像度JPG (.jpg)
• フォトショップ形式 (.psd)
補足説明
マウスピース矯正を マウスピース型矯正装置
クリアフィット をマウスピース型矯正装置(クリアフィット)

※医療広告の関係で表記を統一してください。
用語は、マウスピース型矯正装置(クリアフィット)を徹底してください。

高校生~20代女性に響くような デザインが希望です。

透明で見ないこと 取り外せること
最新式 3Dスキャンナー dento scoopeを導入していること
dento scope により、簡易シュミレーションが見れること
裏側矯正も得意なことから 組み合わせることによって対応できる
幅が広がったこと。

を強調したデザインが希望です。

参照https://www.kirari-ha.jp/simulation/

なるべく裏側矯正の内容は、記載しないでマウスピース型矯正装置(クリアフィット)の内容だけにしたい。

よろしくお願いします。

```html
<!DOCTYPE html>
<html lang="ja">
<head>
<meta charset="utf-8">
<title>ルーチェ歯科</title>
<link href="https://fonts.googleapis.com/css2?family=Cormorant+Garamond:wght@400;500&family=Noto+Sans+JP:wght@300;400;500&family=Noto+Serif+JP:wght@400;500&display=swap" rel="stylesheet">
<style>
:root{
  --blue:#7fb9e0;
  --blue-soft:#a9d3ef;
  --blue-pale:#eaf4fb;
  --navy:#4f84ad;
  --gold:#b7a27c;
  --text:#555b61;
  --muted:#8b9096;
  --line:#dcdfe2;
  --paper:#ffffff;
  --gray:#f4f5f6;
  --footer:#eef0f2;
}
*{margin:0;padding:0;box-sizing:border-box}
html,body{width:1200px;height:4216px;overflow:hidden}
body{position:relative;background:var(--paper);color:var(--text);font-family:"Noto Sans JP",sans-serif;font-weight:300;font-size:13px;line-height:2}
.abs{position:absolute}
.en{font-family:"Cormorant Garamond",serif;letter-spacing:.12em}

/* header */
.site-header{left:0;top:0;width:1200px;height:60px;background:rgba(255,255,255,.92);z-index:5;display:flex;align-items:center;padding:0 40px}
.brand{font-family:"Noto Sans JP",sans-serif;font-weight:500;font-size:20px;letter-spacing:.04em;color:var(--navy)}
.gnav{margin-left:auto;display:flex}
.gnav a{display:block;width:92px;text-align:center;font-size:12px;color:var(--text);text-decoration:none;border-left:1px solid var(--line);line-height:20px}
.gnav a:last-child{border-right:1px solid var(--line)}
.dropdown{left:766px;top:60px;width:130px;background:#fff;z-index:6;box-shadow:0 4px 10px rgba(0,0,0,.06);padding:8px 0;list-style:none}
.dropdown li{font-size:11px;line-height:1.6;padding:6px 14px;border-bottom:1px dotted var(--line);white-space:nowrap}
.dropdown li:last-child{border:0}

/* hero */
.hero-visual{left:0;top:0;width:1200px;height:580px;background:linear-gradient(120deg,#e9e4df 0%,#f6f2ee 40%,#dfe7ee 75%,#cdd9e3 100%)}
.hero-copy{left:0;top:290px;width:1200px;text-align:center;color:#fff}
.hero-copy .label{font-size:13px;letter-spacing:.2em;line-height:1.6;margin-bottom:10px;text-shadow:0 1px 4px rgba(0,0,0,.25)}
.hero-copy h1{font-family:"Noto Serif JP",serif;font-weight:400;font-size:42px;line-height:1.45;letter-spacing:.06em;text-shadow:0 2px 8px rgba(60,60,60,.3)}
.btn{display:block;width:280px;height:48px;border:1px solid var(--line);border-radius:24px;background:#fff;text-align:center;line-height:46px;font-size:12px;letter-spacing:.15em;color:var(--text);text-decoration:none}
.btn::after{content:"→";margin-left:18px;color:var(--gold)}
.hero-btn{left:460px;top:500px}

/* cards */
.card{background:#fff;box-shadow:0 6px 24px rgba(120,140,160,.12)}
.sec-label{font-size:12px;color:var(--gold)}
.sec-label::before{content:"";display:inline-block;width:34px;height:1px;background:var(--gold);vertical-align:middle;margin-right:10px}
.sec-title{font-family:"Noto Serif JP",serif;font-weight:400;color:var(--navy);font-size:26px;line-height:1.5;letter-spacing:.05em;margin:8px 0 18px}
.body-text{font-size:12.5px;line-height:2.1;color:var(--text)}

.intro-card{left:160px;top:740px;width:510px;height:440px;padding:46px 48px}
.intro-card .btn{margin:28px 0 0 60px}
.aligner{left:700px;top:790px;width:420px;height:260px}
.side-num{left:1160px;top:740px;font-size:22px;color:#c9ccd0}

.mix-band{left:0;top:1240px;width:1200px;height:450px;background:linear-gradient(180deg,#fff 0%,var(--gray) 30%,var(--gray) 100%)}
.retainer{left:0;top:1370px;width:560px;height:300px}
.mix-card{left:600px;top:1290px;width:540px;height:340px;padding:40px 48px}
.mix-card .btn{margin:24px 0 0 70px}

.scan-card{left:100px;top:1730px;width:610px;height:740px;padding:50px 56px}
.scan-card .sec-title{margin-top:18px}
.scan-card .btn{position:absolute;left:165px;top:560px}
.scanner-name{left:740px;top:1762px;font-size:20px;font-weight:400;color:var(--navy);line-height:1.6}
.scanner-img{left:740px;top:1810px;width:400px;height:320px}

.other-head{left:0;top:2620px;width:1200px;text-align:center}
.other-head .en{font-size:13px;color:var(--gold)}
.other-head h2{font-family:"Noto Serif JP",serif;font-weight:400;color:var(--navy);font-size:26px;letter-spacing:.1em}
.other-card{top:2720px;width:480px;height:300px;padding:40px 48px;background:#faf8f5}
.other-card h3{font-family:"Noto Serif JP",serif;font-weight:400;color:var(--navy);font-size:22px;margin-bottom:14px}
.other-card .btn{margin:24px 0 0 52px}

.news-head{left:130px;top:3160px}
.news-head .en{font-size:13px;color:var(--gold)}
.news-head h2{font-family:"Noto Serif JP",serif;font-weight:400;color:var(--navy);font-size:24px;letter-spacing:.1em;line-height:1.5}
.news-head a{font-size:11px;color:var(--muted)}
.news-list{left:350px;top:3150px;width:720px;list-style:none}
.news-list li{display:flex;align-items:center;height:52px;border-bottom:1px solid var(--line);font-size:12.5px}
.news-list time{width:100px;color:var(--muted);font-size:11px}
.news-list .tag{width:46px;height:18px;background:var(--blue-soft);margin-right:18px}

.contact{left:100px;top:3520px;width:1000px;height:440px;background:var(--blue);color:#fff;text-align:center;padding-top:48px}
.contact .en{font-size:13px;opacity:.85}
.contact h2{font-family:"Noto Serif JP",serif;font-weight:400;font-size:28px;letter-spacing:.1em;line-height:1.5}
.contact p{font-size:12px;line-height:2;margin:22px 0}
.contact-row{display:flex;align-items:center;justify-content:center;gap:90px;margin-top:28px}
.tel{font-family:"Cormorant Garamond",serif;font-size:46px;letter-spacing:.06em;text-align:left;line-height:1}
.tel small{display:block;font-family:"Noto Sans JP",sans-serif;font-size:11px;margin-top:8px}
.mail-btn{width:300px;height:56px;border-radius:28px;background:#fff;color:var(--navy);line-height:56px;font-size:13px;letter-spacing:.1em}

.site-footer{left:0;top:3990px;width:1200px;height:226px;background:var(--footer)}
.f-brand{left:130px;top:4012px;font-family:"Noto Sans JP",sans-serif;font-weight:500;font-size:22px;letter-spacing:.04em;color:var(--navy);line-height:1.6}
.f-info{left:130px;top:4058px;font-size:11px;line-height:1.8;color:var(--text)}
.f-sns{left:170px;top:4136px;display:flex;gap:14px}
.f-sns span{width:36px;height:36px;border-radius:50%;background:var(--blue-soft)}
.f-nav{top:4016px;list-style:none;font-size:11.5px;line-height:2.2}
.f-nav li::before{content:"";display:inline-block;width:5px;height:5px;border-radius:50%;background:var(--blue);margin-right:8px;vertical-align:middle}
.copyright{left:0;top:4186px;width:1200px;height:30px;background:var(--navy);color:#fff;text-align:center;font-size:10px;line-height:30px;letter-spacing:.05em}
</style>
</head>
<body>

<div class="abs hero-visual" role="img" aria-label="透明なマウスピース型矯正装置を手にした口元の写真"></div>

<header class="abs site-header">
  <div class="brand">ルーチェ歯科</div>
  <nav class="gnav">
    <a>初診案内</a><a>治療内容</a><a>費用</a><a>医院紹介</a><a>アクセス</a><a>FAQ</a>
  </nav>
</header>
<ul class="abs dropdown">
  <li>マウスピース型矯正</li><li>部分矯正</li><li>裏側矯正</li>
</ul>

<div class="abs hero-copy">
  <p class="label">透明で目立たない、取り外せる</p>
  <h1>マウスピース型矯正装置で<br>笑顔の暮らしをご提案します。</h1>
</div>
<a class="abs btn hero-btn">詳しく見る</a>

<section>
  <div class="abs card intro-card">
    <p class="sec-label en">What's Aligner?</p>
    <h2 class="sec-title">マウスピース型矯正装置って？</h2>
    <p class="body-text">マウスピース型矯正装置（クリアフィット）は、透明で目立たず、食事や歯みがきの際に取り外せるのが特長です。金属のワイヤーを使わないため、痛みや違和感が少なく、学校やお仕事中も気にせず過ごせます。<br>当院では一人ひとりの歯並びに合わせて、無理のない治療計画をご提案いたします。まずはお気軽にご相談ください。</p>
    <a class="btn">詳しく見る</a>
  </div>
  <div class="abs aligner" role="img" aria-label="透明なマウスピース型矯正装置の写真" style="background:radial-gradient(ellipse at center,#e6eef4 0%,#f4f8fb 55%,#fff 80%)"></div>
  <div class="abs side-num en">#2</div>
</section>

<section>
  <div class="abs mix-band"></div>
  <div class="abs retainer" role="img" aria-label="歯型模型と青い矯正装置の写真" style="background:linear-gradient(135deg,#cfe4f1 0%,#8fc3e6 45%,#bcd6e8 100%)"></div>
  <div class="abs card mix-card">
    <p class="sec-label en">Mix Treatment</p>
    <h2 class="sec-title">裏側矯正と合わせて<br>より幅広くご対応します</h2>
    <p class="body-text">裏側矯正を得意とする当院では、マウスピース型矯正装置（クリアフィット）と組み合わせることで、より多くの歯並びのお悩みに対応できるようになりました。見えない矯正をご希望の方もご相談ください。</p>
    <a class="btn">詳しく見る</a>
  </div>
</section>

<section>
  <div class="abs card scan-card">
    <p class="sec-label en">Digital Scanner</p>
    <h2 class="sec-title">最新式デジタルスキャナー<br>“dento scope”を使用</h2>
    <p class="body-text">当院では最新式の3Dスキャナー“dento scope”を導入しています。従来のような粘土状の材料による型取りが不要で、短時間で精密な歯のデータを取得できます。<br>スキャンしたデータから、治療後の歯並びを簡易シミュレーションでご覧いただけます。治療のゴールをイメージしながら、安心して矯正を始めていただけます。</p>
    <a class="btn">詳しく見る</a>
  </div>
  <div class="abs scanner-name">dento scope</div>
  <div class="abs scanner-img" role="img" aria-label="スキャナー本体とモニターに映る歯列の3D画像" style="background:linear-gradient(160deg,#f3f5f7 0%,#e4e9ee 60%,#f6f7f8 100%)"></div>
</section>

<section>
  <div class="abs other-head">
    <p class="en">Other Treatment</p>
    <h2>その他の治療</h2>
  </div>
  <div class="abs other-card" style="left:100px">
    <h3>部分矯正</h3>
    <p class="body-text">前歯のすき間やねじれなど、気になる部分だけを短期間で整える治療です。費用や期間を抑えたい方におすすめです。</p>
    <a class="btn">詳しく見る</a>
  </div>
  <div class="abs other-card" style="left:620px">
    <h3>それ以外の通常診療</h3>
    <p class="body-text">虫歯や歯周病の治療、定期検診やクリーニングなど、お口の健康を守るための一般診療も行っております。</p>
    <a class="btn">詳しく見る</a>
  </div>
</section>

<section>
  <div class="abs news-head">
    <p class="en">News</p>
    <h2>新着情報</h2>
    <a>一覧を見る →</a>
  </div>
  <ul class="abs news-list">
    <li><time>2024.12.25</time><span class="tag"></span>年末年始の診療について</li>
    <li><time>2024.12.20</time><span class="tag"></span>診療時間を変更しました。</li>
    <li><time>2024.12.15</time><span class="tag"></span>初めての矯正相談会のお知らせ</li>
    <li><time>2024.12.10</time><span class="tag"></span>院内サイトをリニューアルしました。</li>
  </ul>
</section>

<section class="abs contact">
  <p class="en">Contact</p>
  <h2>ご相談・お問い合わせ</h2>
  <p>治療に関するご質問やご予約は、お電話またはメールにて承っております。<br>お一人で悩まず、まずはお気軽にご相談ください。</p>
  <div class="contact-row">
    <div class="tel">
      <svg width="34" height="34" viewBox="0 0 24 24" fill="#fff" style="vertical-align:middle;margin-right:6px"><path d="M6.6 10.8a15.1 15.1 0 0 0 6.6 6.6l2.2-2.2c.3-.3.7-.4 1-.2 1.1.4 2.3.6 3.6.6.6 0 1 .4 1 1V20c0 .6-.4 1-1 1A17 17 0 0 1 3 4c0-.6.4-1 1-1h3.5c.6 0 1 .4 1 1 0 1.3.2 2.5.6 3.6.1.3 0 .7-.2 1z"/></svg>03-5812-4470
      <small>受付時間 10:00〜19:00（休診日：木・日・祝）</small>
    </div>
    <div class="mail-btn">メールで問い合わせる →</div>
  </div>
</section>

<footer>
  <div class="abs site-footer"></div>
  <div class="abs f-brand">ルーチェ歯科</div>
  <p class="abs f-info">神田ルーチェ歯科医院<br>東京都千代田区神田小川町3-9-2<br>TEL 03-5812-4470</p>
  <div class="abs f-sns"><span></span><span></span></div>
  <ul class="abs f-nav" style="left:760px">
    <li>初診案内</li><li>治療内容</li><li>費用</li><li>マウスピース型矯正</li><li>部分矯正</li>
  </ul>
  <ul class="abs f-nav" style="left:960px">
    <li>医院紹介</li><li>アクセス</li><li>FAQ</li><li>新着情報</li>
  </ul>
  <div class="abs copyright">Copyright © 2024 神田ルーチェ歯科医院 All Rights Reserved.</div>
</footer>

</body>
</html>
```